Pull Up Banners

Would like to have these pull up banner designs changed to a new modern theme. I have running a sales booth and want to re-design the banner designs. I have uploaded old banner design, I need phone number and website added onto bottom. Happy to consider images to attract people attention to increase sales and spark people interest walking past.

```html
<!DOCTYPE html>
<html lang="en">
<head>
<meta charset="utf-8">
<title>Korvale Pull Up Banners</title>
<link rel="stylesheet" href="https://fonts.googleapis.com/css2?family=Baloo+2:wght@600;700&family=Montserrat:wght@500;700&display=swap">
<style>
  :root{
    --stage:#b9bec3;
    --panel:#111111;
    --orange:#e85d10;
    --cyan:#4cc6ea;
    --white:#ffffff;
    --ink:#0b0b0b;
  }
  *{box-sizing:border-box;margin:0;padding:0}
  html,body{width:1200px;height:848px;overflow:hidden}
  body{background:var(--stage);position:relative;font-family:"Baloo 2",sans-serif}
  .banner{position:absolute;top:79px;width:300px;height:662px;background:var(--panel);overflow:hidden}
  .banner--phone{left:150px}
  .banner--managed{left:750px}

  .brand{position:absolute;top:12px;left:0;width:100%;display:flex;align-items:center;justify-content:center;gap:10px}
  .brand__dot{width:28px;height:28px;border-radius:50%;background:var(--orange)}
  .brand__text{display:flex;flex-direction:column;align-items:flex-start}
  .brand__name{font-family:"Montserrat",sans-serif;font-weight:700;font-size:24px;letter-spacing:3px;color:var(--orange);line-height:1}
  .brand__tagline{font-family:"Montserrat",sans-serif;font-weight:500;font-size:5.4px;letter-spacing:1px;color:var(--white);margin-top:3px}

  .hero{position:absolute;left:10px;top:58px;width:280px;height:246px}

  .title{position:absolute;top:318px;text-align:center;font-family:"Montserrat",sans-serif;font-weight:700;color:var(--cyan);letter-spacing:.5px;border-top:1.5px solid var(--cyan);border-bottom:1.5px solid var(--cyan)}
  .banner--phone .title{left:38px;right:28px;font-size:18px;line-height:19px;padding:6px 0}
  .banner--managed .title{left:38px;right:20px;font-size:17.5px;line-height:19px;padding:5px 0 6px}

  .service{position:absolute;width:140px;transform:translateX(-50%);text-align:center;color:var(--cyan);font-weight:700;font-size:15.5px;line-height:18px}
  .banner--managed .service{font-size:15px;line-height:18px}
  .service__icon{display:block;width:36px;height:36px;margin:0 auto 9px}
  .banner--managed .service__icon{margin-bottom:7px}

  .contact-band{position:absolute;left:10px;top:563px;width:280px;height:68px}
  .contact-band__curve{position:absolute;inset:0;width:100%;height:100%}
  .contact-band__phone{position:absolute;left:0;right:0;bottom:9px;display:flex;align-items:center;justify-content:center;gap:4px;font-family:"Montserrat",sans-serif;font-weight:700;font-size:15px;color:var(--ink);letter-spacing:.5px}
  .contact-band__icon{width:18px;height:18px;flex:none}
  .website{position:absolute;left:0;right:0;top:636px;text-align:center;font-family:"Montserrat",sans-serif;font-weight:700;font-size:14px;color:var(--cyan)}
</style>
</head>
<body>

<svg width="0" height="0" style="position:absolute" aria-hidden="true">
  <defs>
    <linearGradient id="icon-fill" x1="0" y1="0" x2="0" y2="1">
      <stop offset="0" stop-color="#5fd0f5"/>
      <stop offset="1" stop-color="#1e7fd8"/>
    </linearGradient>
    <radialGradient id="hero-fill" cx="0.5" cy="0.4" r="0.7">
      <stop offset="0" stop-color="#2f7fe0"/>
      <stop offset="0.55" stop-color="#10479e"/>
      <stop offset="1" stop-color="#061530"/>
    </radialGradient>
    <linearGradient id="band-fill" x1="0" y1="0" x2="0" y2="1">
      <stop offset="0" stop-color="#1a5fd0"/>
      <stop offset="1" stop-color="#2bc0f4"/>
    </linearGradient>
  </defs>
</svg>

<!-- Banner 1: Cloud phone system -->
<section class="banner banner--phone">
  <header class="brand">
    <span class="brand__dot"></span>
    <div class="brand__text">
      <span class="brand__name">KORVALE</span>
      <span class="brand__tagline">YOUR TRUSTED PARTNER FOR EVERY I.T NEED</span>
    </div>
  </header>

  <svg class="hero" viewBox="0 0 280 254" preserveAspectRatio="none">
    <path d="M0 64 Q130 -38 280 18 L280 254 L0 254Z" fill="#ffffff"/>
    <path d="M0 68 Q130 -28 280 28 L280 254 L0 254Z" fill="#e85d10"/>
    <path d="M0 70 Q140 -12 280 74 L280 254 L0 254Z" fill="url(#hero-fill)" role="img" aria-label="Illustration of a digital hand touching a glowing tools icon ringed by service icons"/>
  </svg>

  <h2 class="title">CLOUD PHONE SYSTEM<br>&amp; INTERNET</h2>

  <div class="service" style="left:90px;top:383px">
    <svg class="service__icon" viewBox="0 0 36 36"><circle cx="18" cy="18" r="18" fill="url(#icon-fill)"/><path d="M12 10c1-1 2-1 3 0l2 3c.5 1 0 2-1 2.5-.5.3-.5 1 0 2l2.5 2.5c1 .5 1.7.5 2 0 .5-1 1.5-1.5 2.5-1l3 2c1 1 1 2 0 3-2 2-5 2-9-2s-7-8-5-12z" fill="#fff"/><path d="M20 9a7 7 0 0 1 7 7M20 12a4 4 0 0 1 4 4" stroke="#fff" stroke-width="1.5" fill="none"/></svg>
    VoIP &amp; Phone<br>Systems
  </div>
  <div class="service" style="left:213px;top:383px">
    <svg class="service__icon" viewBox="0 0 36 36"><circle cx="18" cy="18" r="18" fill="url(#icon-fill)"/><path d="M9 10h18v13H16l-5 4v-4H9z" fill="#fff"/><path d="M12 14h12M12 17h12M12 20h8" stroke="#2a8ee0" stroke-width="1.4"/></svg>
    SMS<br>Gateway
  </div>
  <div class="service" style="left:90px;top:481px">
    <svg class="service__icon" viewBox="0 0 36 36"><circle cx="18" cy="18" r="18" fill="url(#icon-fill)"/><circle cx="18" cy="13" r="3.5" fill="#fff"/><circle cx="11" cy="15" r="2.6" fill="#fff"/><circle cx="25" cy="15" r="2.6" fill="#fff"/><path d="M12 25a6 6 0 0 1 12 0z" fill="#fff"/><path d="M6 25a5 5 0 0 1 8-4v4zM30 25a5 5 0 0 0-8-4v4z" fill="#fff"/></svg>
    Unified<br>Group Calling
  </div>
  <div class="service" style="left:213px;top:481px">
    <svg class="service__icon" viewBox="0 0 36 36"><circle cx="18" cy="18" r="18" fill="url(#icon-fill)"/><g stroke="#fff" stroke-width="2.2" fill="none" stroke-linecap="round"><path d="M8 15a14 14 0 0 1 20 0"/><path d="M11.5 18.5a9 9 0 0 1 13 0"/><path d="M15 22a4 4 0 0 1 6 0"/></g><circle cx="18" cy="25.5" r="1.8" fill="#fff"/></svg>
    Broadband, Fibre &amp;<br>4G Internet
  </div>

  <div class="contact-band">
    <svg class="contact-band__curve" viewBox="0 0 280 68" preserveAspectRatio="none"><path d="M0 8 Q140 58 280 0 L280 68 L0 68Z" fill="url(#band-fill)"/></svg>
    <div class="contact-band__phone">
      <svg class="contact-band__icon" viewBox="0 0 24 24"><path d="M5 3c1-1 2-1 3 0l2 3c.5 1 0 2-1 2.5-.5.3-.5 1 0 2l2.5 2.5c1 .5 1.7.5 2 0 .5-1 1.5-1.5 2.5-1l3 2c1 1 1 2 0 3-2 2-5 2-9-2S3 5 5 3z" fill="#0b0b0b"/><path d="M14 3a7 7 0 0 1 7 7M14 6a4 4 0 0 1 4 4" stroke="#0b0b0b" stroke-width="1.6" fill="none"/></svg>
      <span>1300 555 019</span>
    </div>
  </div>
  <p class="website">korvaletech.com.au</p>
</section>

<!-- Banner 2: Managed IT services -->
<section class="banner banner--managed">
  <header class="brand">
    <span class="brand__dot"></span>
    <div class="brand__text">
      <span class="brand__name">KORVALE</span>
      <span class="brand__tagline">YOUR TRUSTED PARTNER FOR EVERY I.T NEED</span>
    </div>
  </header>

  <svg class="hero" viewBox="0 0 280 254" preserveAspectRatio="none">
    <path d="M0 64 Q130 -38 280 18 L280 254 L0 254Z" fill="#ffffff"/>
    <path d="M0 68 Q130 -28 280 28 L280 254 L0 254Z" fill="#e85d10"/>
    <path d="M0 70 Q140 -12 280 74 L280 254 L0 254Z" fill="url(#hero-fill)" role="img" aria-label="Illustration of a digital hand touching a glowing tools icon ringed by service icons"/>
  </svg>

  <h2 class="title">MANAGED I.T SERVICES</h2>

  <div class="service" style="left:82px;top:350px">
    <svg class="service__icon" viewBox="0 0 36 36"><circle cx="18" cy="18" r="18" fill="url(#icon-fill)"/><path d="M18 7l9 3.5v6.5c0 6-4 10-9 12-5-2-9-6-9-12v-6.5z" fill="none" stroke="#fff" stroke-width="1.8"/><rect x="14" y="16.5" width="8" height="6.5" rx="1" fill="#fff"/><path d="M15.5 16.5v-2a2.5 2.5 0 0 1 5 0v2" stroke="#fff" stroke-width="1.5" fill="none"/></svg>
    Cybersecurity<br>Solutions
  </div>
  <div class="service" style="left:218px;top:350px">
    <svg class="service__icon" viewBox="0 0 36 36"><circle cx="18" cy="18" r="18" fill="url(#icon-fill)"/><path d="M11 21a4 4 0 0 1 0-8 6 6 0 0 1 11.5-1.5A4.8 4.8 0 0 1 25 21z" fill="none" stroke="#fff" stroke-width="1.8"/><path d="M14 21v5M18 21v6M22 21v5" stroke="#fff" stroke-width="1.5"/><circle cx="14" cy="27" r="1.4" fill="#fff"/><circle cx="18" cy="28" r="1.4" fill="#fff"/><circle cx="22" cy="27" r="1.4" fill="#fff"/></svg>
    Cloud Servers<br>&amp; Backups
  </div>
  <div class="service" style="left:150px;top:424px">
    <svg class="service__icon" viewBox="0 0 36 36"><circle cx="18" cy="18" r="18" fill="url(#icon-fill)"/><rect x="9" y="10" width="18" height="12" rx="1.5" fill="none" stroke="#fff" stroke-width="1.8"/><path d="M16 22l-1 4h6l-1-4M13 26.5h10" stroke="#fff" stroke-width="1.6" fill="none"/></svg>
    Managed<br>I.T Support
  </div>
  <div class="service" style="left:82px;top:496px">
    <svg class="service__icon" viewBox="0 0 36 36"><circle cx="18" cy="18" r="18" fill="url(#icon-fill)"/><rect x="9" y="11" width="18" height="14" rx="1.5" fill="#fff"/><path d="M9.5 12l8.5 7 8.5-7" stroke="#2a8ee0" stroke-width="1.6" fill="none"/></svg>
    Office Suite<br>Email Packs
  </div>
  <div class="service" style="left:218px;top:496px">
    <svg class="service__icon" viewBox="0 0 36 36"><circle cx="18" cy="18" r="18" fill="url(#icon-fill)"/><g fill="none" stroke="#fff" stroke-width="1.5"><circle cx="17" cy="17" r="8"/><ellipse cx="17" cy="17" rx="3.5" ry="8"/><path d="M9 17h16M10.5 13h13M10.5 21h13"/></g><path d="M22 21l6 2.5-2.5 1 2 2.5-1.2 1-2-2.5-1.3 2z" fill="#fff"/></svg>
    Domains &amp;<br>Websites
  </div>

  <div class="contact-band">
    <svg class="contact-band__curve" viewBox="0 0 280 68" preserveAspectRatio="none"><path d="M0 8 Q140 58 280 0 L280 68 L0 68Z" fill="url(#band-fill)"/></svg>
    <div class="contact-band__phone">
      <svg class="contact-band__icon" viewBox="0 0 24 24"><path d="M5 3c1-1 2-1 3 0l2 3c.5 1 0 2-1 2.5-.5.3-.5 1 0 2l2.5 2.5c1 .5 1.7.5 2 0 .5-1 1.5-1.5 2.5-1l3 2c1 1 1 2 0 3-2 2-5 2-9-2S3 5 5 3z" fill="#0b0b0b"/><path d="M14 3a7 7 0 0 1 7 7M14 6a4 4 0 0 1 4 4" stroke="#0b0b0b" stroke-width="1.6" fill="none"/></svg>
      <span>1300 555 019</span>
    </div>
  </div>
  <p class="website">korvaletech.com.au</p>
</section>

</body>
</html>
```